Book Cover Design Project

A non-fiction book on child protection, specifically... keeping young children safe from predators and keeping teenagers safe from themselves.

Title:
Under Our Roof

Subtitle:
A Guide To Keeping Your Children Safe

Author:
Martin Kellerby

```html
<!DOCTYPE html>
<html lang="en">
<head>
<meta charset="utf-8">
<title>Under Our Roof — Book Cover</title>
<link rel="stylesheet" href="https://fonts.googleapis.com/css2?family=Anton&family=Archivo+Black&display=swap">
<style>
  :root {
    --sky-blue: #00b0f0;
    --paper: #ffffff;
    --ink-grey: #4a4a4a;
    --photo-light: #fbfbfb;
    --photo-shade: #ececec;
    --canvas-bg: #ffffff;
  }
  * { margin: 0; padding: 0; box-sizing: border-box; }
  html, body {
    width: 1000px;
    height: 1200px;
    overflow: hidden;
    background: var(--canvas-bg);
  }
  .book-cover {
    position: absolute;
    left: 140px;
    top: 18px;
    width: 768px;
    height: 1154px;
    background: var(--paper);
    overflow: hidden;
  }
  .author-band {
    height: 125px;
    background: var(--sky-blue);
    display: flex;
    align-items: center;
    justify-content: center;
  }
  .author-name {
    font-family: "Archivo Black", sans-serif;
    font-size: 58px;
    color: var(--paper);
    letter-spacing: 0.5px;
    line-height: 1;
  }
  .cover-photo {
    position: absolute;
    left: 14px;
    top: 165px;
    width: 750px;
    height: 440px;
    background: linear-gradient(180deg, var(--photo-light) 0%, var(--photo-light) 70%, var(--photo-shade) 100%);
  }
  .title-block {
    position: absolute;
    right: 28px;
    top: 600px;
    text-align: right;
  }
  .book-title {
    font-family: "Anton", sans-serif;
    font-weight: 400;
    color: var(--sky-blue);
    line-height: 0.95;
    text-shadow: 1px 2px 2px rgba(0, 0, 0, 0.12);
  }
  .book-title .title-line { display: block; }
  .book-title .title-line--first { font-size: 215px; }
  .book-title .title-line--second { font-size: 175px; }
  .book-subtitle {
    font-family: "Archivo Black", sans-serif;
    font-size: 44px;
    line-height: 1.45;
    color: var(--ink-grey);
    margin-top: 6px;
  }
  .book-subtitle .subtitle-line { display: block; }
</style>
</head>
<body>
  <main class="book-cover">
    <header class="author-band">
      <p class="author-name">Martin Kellerby</p>
    </header>

    <div class="cover-photo" role="img"
         aria-label="Photograph of seven smiling young children in colourful clothes standing in a row against a white wall, holding hands"></div>

    <section class="title-block">
      <h1 class="book-title">
        <span class="title-line title-line--first">Under</span>
        <span class="title-line title-line--second">Our Roof</span>
      </h1>
      <p class="book-subtitle">
        <span class="subtitle-line">A Guide To Keeping Your</span>
        <span class="subtitle-line">Children Safe</span>
      </p>
    </section>
  </main>
</body>
</html>
```